The Perfect Business Card for PineHarbor

I am looking for a business card which beautifully incorporates my logo, reflects my business and looks special, elegant and clean.

```html
<!DOCTYPE html>
<html lang="en">
<head>
<meta charset="utf-8">
<title>PineHarbor Business Card</title>
<link rel="stylesheet" href="https://fonts.googleapis.com/css2?family=Open+Sans:ital,wght@0,300;0,400;0,700;1,400&display=swap">
<style>
  :root {
    --leaf: #84a548;
    --moss: #566b30;
    --olive-text: #5e7a2e;
    --pattern-light: rgba(110, 190, 80, 0.35);
    --pattern-soft: rgba(132, 165, 72, 0);
    --paper: #ffffff;
    --edge: #5a5a5a;
  }
  html, body {
    margin: 0;
    padding: 0;
    width: 1200px;
    height: 1000px;
    overflow: hidden;
    background: var(--paper);
    font-family: "Open Sans", Arial, sans-serif;
  }
  .canvas {
    position: relative;
    width: 1200px;
    height: 1000px;
    overflow: hidden;
  }
  .band {
    position: absolute;
    height: 20px;
    width: 600px;
  }
  .band--top-left { top: 0; left: 0; background: var(--leaf); }
  .band--top-right { top: 0; left: 600px; background: var(--moss); }
  .band--bottom-left { bottom: 0; left: 0; background: var(--moss); }
  .band--bottom-right { bottom: 0; left: 600px; background: var(--leaf); }

  .card {
    position: absolute;
    width: 707px;
    height: 393px;
    overflow: hidden;
  }
  .card--front {
    left: 81px;
    top: 85px;
    background: var(--paper);
    box-shadow: inset 0 0 0 1px var(--edge);
  }
  .card--back {
    left: 426px;
    top: 502px;
    background: var(--leaf);
  }
  .front-shape {
    position: absolute;
    inset: 0;
  }
  .line-texture {
    position: absolute;
  }
  .line-texture--front {
    left: 389px;
    top: 200px;
    width: 317px;
    height: 192px;
    background: linear-gradient(to bottom, var(--pattern-soft), var(--pattern-light));
  }
  .line-texture--back-top {
    left: 0; top: 0; width: 707px; height: 180px;
    background: linear-gradient(to bottom, var(--pattern-light), var(--pattern-soft));
  }
  .line-texture--back-bottom {
    left: 0; bottom: 0; width: 707px; height: 190px;
    background: linear-gradient(to top, var(--pattern-light), var(--pattern-soft));
  }

  .brand {
    position: absolute;
    display: flex;
    align-items: center;
    gap: 14px;
  }
  .brand__dot {
    width: 70px;
    height: 70px;
    border-radius: 50%;
    box-sizing: border-box;
    border: 2px solid currentColor;
  }
  .brand__name {
    font-size: 40px;
    font-weight: 400;
    letter-spacing: 0.5px;
    line-height: 1;
  }
  .brand--front { left: 38px; top: 160px; color: var(--olive-text); }
  .brand--back { left: 180px; top: 145px; color: var(--paper); }

  .contact-block {
    position: absolute;
    left: 445px;
    color: var(--paper);
    border-left: 2px solid var(--paper);
    padding-left: 19px;
  }
  .identity { top: 131px; }
  .identity__name {
    margin: 0;
    font-size: 24px;
    font-weight: 700;
    line-height: 26px;
  }
  .identity__role {
    margin: 0;
    font-size: 16px;
    font-weight: 300;
    line-height: 20px;
  }
  .contact-details {
    top: 193px;
    list-style: none;
    margin: 0;
    font-size: 15px;
    font-weight: 300;
    line-height: 25px;
  }
  .website {
    position: absolute;
    left: 0;
    width: 707px;
    top: 256px;
    text-align: center;
    margin: 0;
    color: var(--paper);
    font-size: 17px;
    font-style: italic;
    font-weight: 400;
    padding-right: 30px;
    box-sizing: border-box;
  }
</style>
</head>
<body>
<main class="canvas">
  <div class="band band--top-left"></div>
  <div class="band band--top-right"></div>

  <section class="card card--front" aria-label="Business card front">
    <svg class="front-shape" width="707" height="393" viewBox="0 0 707 393" aria-hidden="true">
      <polygon fill="var(--moss)" points="381,0 707,0 707,393 381,393 381,235 341,195 381,155"/>
      <polygon fill="var(--leaf)" points="389,0 707,0 707,393 389,393 389,232 352,195 389,158"/>
    </svg>
    <div class="line-texture line-texture--front" role="img" aria-label="Fine crossing line texture"></div>

    <div class="brand brand--front">
      <span class="brand__dot"></span>
      <span class="brand__name">PineHarbor</span>
    </div>

    <div class="contact-block identity">
      <p class="identity__name">Pine Harbor</p>
      <p class="identity__role">General Manager</p>
    </div>
    <ul class="contact-block contact-details">
      <li>0123456789</li>
      <li>email@email.com</li>
      <li>www.web.com</li>
    </ul>
  </section>

  <section class="card card--back" aria-label="Business card back">
    <div class="line-texture line-texture--back-top" role="img" aria-label="Fine crossing line texture"></div>
    <div class="line-texture line-texture--back-bottom" role="img" aria-label="Fine crossing line texture"></div>
    <div class="brand brand--back">
      <span class="brand__dot"></span>
      <span class="brand__name">PineHarbor</span>
    </div>
    <p class="website">www.pineharbor.com</p>
  </section>

  <div class="band band--bottom-left"></div>
  <div class="band band--bottom-right"></div>
</main>
</body>
</html>
```